Healing Arts Brochure with Simple, Elegant, Zen Design ,

I need to create a brochure for an upcoming event and I have to complete this project in the next few days.
I would like a tri-fold or z fold type of brochure- standard size of 8.5 x 11- both sides with text

i would like the overall design to be simple, elegant and zen .... yet not too plain :-))
I would like the fonts used to be clean and clear and ... easy to read.
I would like the background color to be white/cream or light color
Please do not use too many colors when working with the descriptions of my services or break those sections up too much ... a little is ok.
I don't want the brochure to be busy

I've uploaded the text, my photo, a photo that I will be using on my website, my logo symbol without my name and several logo symbols with my name in different font styles. I am not wed to any of the various font styles of the logo just yet.
TEXT FILE IS UPLOADED

Dear Designers, The design submissions that I'm receiving so far have not been including all 3 pages of text in the brochure. I pulled my text file to update it with the instructions that there are 3 pages of text information that need to be on the brochure. Unfortunately, I'm not able to upload the text file - seems to be a glitch on the ArtMarkly website.. I called for support and they won't get back to me for a couple of hours. That will be around 11:00 am PST in the USA. PLEASE CHECK BACK if you haven't already downloaded the text file. Otherwise, please add the missing information and resubmit your ideas. Thank you!! MR

Target Market(s)

My services target clients in the healing arts.

Industry/Entity Type

Event

Requirements
Must have
• Please include the colors tones of my logo and the sunset photo -golds, oranges, blues
Brochure must include my photo and the sunset photo
Should not have
• Objects like teacups etc. that have nothing to do with my services - thank you kindly
I don't want any other photos or objects on the brochure other than my photo and the sun
Please don't put the tagline in quotes
Please do not make the brochure busy with too many colors in the text.

```html
<!DOCTYPE html>
<html lang="en">
<head>
<meta charset="utf-8">
<title>Healing Arts Brochure – Inside Panels</title>
<link href="https://fonts.googleapis.com/css2?family=Delius&family=Arimo:wght@400&display=swap" rel="stylesheet">
<style>
  :root{
    --paper:#fffdf1;
    --ink:#2f2f2f;
    --heading-ink:#3f5480;
    --band-start:#fbe7a6;
    --band-end:#fffbe8;
    --bullet:#f3c27a;
    --gold:#f6c21a;
    --amber:#f0a21b;
    --orange:#e8711c;
    --deep-orange:#e25d12;
  }
  html,body{margin:0;padding:0;overflow:hidden;}
  body{width:1200px;height:931px;background:var(--paper);position:relative;font-family:"Arimo",Arial,sans-serif;color:var(--ink);}
  .panel{position:absolute;top:0;width:329px;}
  .panel-left{left:36px;}
  .panel-middle{left:437px;}
  .panel-right{left:834px;}
  .section-title{
    position:absolute;left:0;width:100%;height:38px;box-sizing:border-box;
    padding-left:14px;line-height:40px;
    font-family:"Delius",cursive;font-size:21px;color:var(--heading-ink);
    background:linear-gradient(90deg,var(--band-start),var(--band-end));
    margin:0;font-weight:400;
  }
  .section-title sup{font-size:8px;vertical-align:top;line-height:28px;}
  .copy{position:absolute;left:0;width:100%;margin:0;font-size:17px;line-height:25.3px;}
  .copy .line{display:block;white-space:nowrap;text-align:justify;text-align-last:justify;}
  .copy .line.last{text-align-last:left;}
  .intro{position:absolute;left:0;margin:0;font-size:17px;line-height:21px;}
  .symptoms{position:absolute;left:0;top:83px;margin:0;padding:0;list-style:none;font-size:17px;}
  .symptoms li{position:relative;padding-left:22px;height:33px;line-height:27px;}
  .symptoms li.bullet::before{content:"";position:absolute;left:2px;top:10px;width:9px;height:9px;border-radius:50%;background:var(--bullet);}
  .sunset-band{
    position:absolute;left:0;top:722px;width:1200px;height:108px;
    background:linear-gradient(90deg,var(--amber) 0%,var(--gold) 45%,#f9d862 70%,var(--orange) 100%);
    opacity:.85;
  }
  .brand{position:absolute;left:695px;top:846px;width:200px;text-align:center;}
  .brand-name{font-family:"Delius",cursive;font-size:21px;color:var(--deep-orange);}
</style>
</head>
<body>

<section class="panel panel-left">
  <h2 class="section-title" style="top:40px">Somatic Unwinding<sup>™</sup></h2>
  <p class="copy" style="top:96px">
    <span class="line">Somatic Unwinding is a body-oriented</span>
    <span class="line">approach to resolving the symptoms of</span>
    <span class="line">trauma and chronic stress. Sources of</span>
    <span class="line">trauma are wide-ranging -- including</span>
    <span class="line">accidents; falls; surgeries; injuries;</span>
    <span class="line">physical assault; rape; emotional,</span>
    <span class="line">physical or sexual abuse; loss of a loved</span>
    <span class="line">one; childhood neglect or abuse; difficult</span>
    <span class="line">births; high fever; serious illness; natural</span>
    <span class="line last">disasters, violence and war.</span>
  </p>
  <p class="copy" style="top:382px">
    <span class="line">Trauma occurs when the highly activated</span>
    <span class="line">energy of our body’s survival response</span>
    <span class="line">(fight, flight or freeze) is unable to</span>
    <span class="line">complete and discharge in the aftermath</span>
    <span class="line">of a life- threatening or overwhelming</span>
    <span class="line">experience. The symptoms of trauma are</span>
    <span class="line">a result of this highly charged energy</span>
    <span class="line">remaining “frozen” or stuck as an</span>
    <span class="line">unresolved memory in the neuromuscular</span>
    <span class="line last">systems of the body.</span>
  </p>
</section>

<section class="panel panel-middle">
  <p class="intro" style="top:35px">The symptoms of unresolved trauma<br>can include:</p>
  <ul class="symptoms">
    <li class="bullet">Panic or anxiety</li>
    <li>(including panic attacks)</li>
    <li class="bullet">Hyper-vigilance</li>
    <li class="bullet">Chronic pain of all kinds</li>
    <li class="bullet">Sleep disorders</li>
    <li class="bullet">Chronic tension</li>
    <li class="bullet">Addictions of all kinds</li>
    <li class="bullet">Migraines</li>
    <li class="bullet">Gastrointestinal disorders</li>
    <li class="bullet">Dissociation</li>
    <li class="bullet">And many others</li>
  </ul>
  <h2 class="section-title" style="top:495px">iRenew<sup>®</sup> &amp; Yoga Nidra Meditation</h2>
  <p class="copy" style="top:543px">
    <span class="line">Somatic Unwinding utilizes the</span>
    <span class="line">awareness of body sensations and</span>
    <span class="line">tracking the rhythmic cycles of the</span>
    <span class="line">nervous system to assist in gently and</span>
    <span class="line">slowly discharging the energy of trauma in</span>
    <span class="line">a titrated (small amounts) and supported</span>
  </p>
</section>

<section class="panel panel-right">
  <p class="copy" style="top:32px">
    <span class="line">way. The result is that clients are able to</span>
    <span class="line">“re-negotiate” their trauma in present time</span>
    <span class="line">and thaw the “frozen” or bound energy</span>
    <span class="line">that was the underlying cause of their</span>
    <span class="line">symptoms. Somatic Unwinding</span>
    <span class="line">empowers clients to develop their own</span>
    <span class="line">capacity for self- regulation and the result</span>
    <span class="line">is a return to a greater sense of aliveness,</span>
    <span class="line last">relaxation and resiliency.</span>
  </p>
  <h2 class="section-title" style="top:296px">Sound Therapy</h2>
  <p class="copy" style="top:341px">
    <span class="line">iRenew® (Integrative Renewal) is a</span>
    <span class="line">modern adaption of an ancient meditation</span>
    <span class="line">practice called Yoga Nidra (yogic sleep).</span>
    <span class="line">iRenew® is a research based protocol that</span>
    <span class="line">provides a systematic method for</span>
    <span class="line">promoting healing, stress reduction and</span>
    <span class="line">self-regulation. iRenew® is used in the</span>
    <span class="line">treatment of trauma, P.T.S.D., and many</span>
    <span class="line">stress related illnesses; such as insomnia,</span>
    <span class="line last">chronic pain, anxiety and depression.</span>
  </p>
  <p class="copy" style="top:620px">
    <span class="line">I offer individual sessions of iRenew® and</span>
    <span class="line">personalized instruction in learning the</span>
    <span class="line last">protocol.</span>
  </p>
</section>

<div class="sunset-band" role="img" aria-label="Decorative sunset swoosh in gold and orange tones"></div>

<div class="brand">
  <span class="brand-name">Sunward Healing</span>
</div>

</body>
</html>
```